Landing Page Design for Adult Dating Age Verification (18+)

The objective of this task is to design a visually appealing pre-landing page for the adult dating site "Plumvelle (site: https://plumvelle.example/)" with an age verification mechanism. The pre-landing page will feature two buttons that redirect visitors to the main offer. The design should also include a footer block that includes links to the terms of use, privacy policy, and contact us pages.

Design Requirements:
Develop an age verification section prominently displayed on the pre-landing page.
Design the section to include two buttons labeled "Yes" and "No" for visitors to confirm their age.
Ensure the section is visually appealing and clearly communicates the purpose of age verification.

Visual Appeal:
Create a visually appealing design that aligns with the branding and theme of the "Plumvelle" adult dating site.
Use suitable color schemes, typography, and graphics to enhance the overall visual appeal of the pre-landing page.

Layout and Navigation:
Design an engaging and intuitive layout that encourages visitors to interact with the page and proceed to the main offer.
Ensure clear and visible navigation elements that direct visitors to the main offer or provide additional information.

Responsive Design:
Develop a responsive design that provides a seamless user experience across various devices, including desktop and mobile.
Ensure the design elements and layout adapt well to different screen sizes and resolutions.

File Formats and Assets:
Deliver the final design in PSD, AI, or Sketch format, ensuring that the files are well-organized and layered.
Include any necessary images or assets used in the design, ensuring they are of high quality and optimized for web use.

```html
<!DOCTYPE html>
<html lang="en">
<head>
<meta charset="UTF-8">
<title>Plumvelle — Age Verification</title>
<link href="https://fonts.googleapis.com/css2?family=Barlow+Condensed:wght@300;400;600;700&family=Montserrat:wght@500&family=Lora:wght@600&display=swap" rel="stylesheet">
<style>
  :root {
    --bg-dark: #2c2c2e;
    --bg-mid: #4a4a4c;
    --bg-warm: #5a2a35;
    --text: #ffffff;
    --accent: #e64275;
    --logo-pink: #e7b8e3;
    --frame: rgba(255,255,255,0.75);
  }
  * { margin: 0; padding: 0; box-sizing: border-box; }
  html, body { width: 1200px; height: 669px; overflow: hidden; }
  body {
    position: relative;
    background: var(--bg-dark);
    color: var(--text);
    font-family: "Barlow Condensed", sans-serif;
  }
  .hero-backdrop {
    position: absolute; inset: 0;
    background:
      radial-gradient(ellipse 360px 220px at 820px 220px, rgba(120,30,55,0.55), transparent 70%),
      radial-gradient(ellipse 500px 300px at 450px 250px, rgba(95,85,82,0.55), transparent 75%),
      radial-gradient(ellipse 600px 260px at 650px 620px, rgba(85,85,88,0.6), transparent 75%),
      linear-gradient(160deg, var(--bg-mid) 0%, var(--bg-dark) 55%, #38383a 100%);
  }
  .age-gate {
    position: absolute; inset: 0;
    text-align: center;
  }
  .brand {
    position: absolute; top: 229px; left: 0; right: 0;
    display: flex; justify-content: center; align-items: center; gap: 6px;
  }
  .brand-dot {
    width: 26px; height: 26px; border-radius: 50%;
    background: var(--logo-pink);
  }
  .brand-name {
    font-family: "Lora", serif; font-weight: 600;
    font-size: 17px; color: var(--text);
  }
  .question {
    position: absolute; left: 69px; top: 282px;
    width: 1061px; height: 64px;
    border: 1px dashed var(--frame);
    display: flex; align-items: center; justify-content: center;
    font-size: 45px; font-weight: 300; letter-spacing: 0.3px;
    line-height: 1;
  }
  .question strong { font-weight: 700; margin: 0 10px; }
  .notice {
    position: absolute; top: 361px; left: 0; right: 0;
    font-size: 12.8px; font-weight: 400; letter-spacing: 0.1px;
  }
  .btn {
    position: absolute; top: 417px;
    width: 345px; height: 36px;
    display: flex; align-items: center; justify-content: center;
    font-size: 13px; font-weight: 600; letter-spacing: 0.3px;
    color: var(--text); text-decoration: none;
  }
  .btn-confirm { left: 249px; background: var(--accent); }
  .btn-decline { left: 605px; border: 1px solid var(--frame); }
  .legal {
    position: absolute; top: 474px; left: 0; right: 0;
    font-family: "Montserrat", sans-serif; font-weight: 500;
    font-size: 7.3px; text-transform: uppercase;
  }
  .legal a { color: var(--text); text-decoration: none; }
</style>
</head>
<body>
  <div class="hero-backdrop" role="img" aria-label="Softly lit photograph of a woman in red lingerie lying on white bed sheets, darkened behind the overlay"></div>
  <main class="age-gate">
    <div class="brand"><span class="brand-dot"></span><span class="brand-name">Plumvelle</span></div>
    <h1 class="question">ARE YOU <strong>AT LEAST 18</strong> YEARS OLD</h1>
    <p class="notice">YOU CANNOT ACCESS THIS WEBSITE IF YOU ARE UNDER 18 YEARS OLD.</p>
    <a class="btn btn-confirm" href="https://plumvelle.example/">I AM OVER 18 YEARS</a>
    <a class="btn btn-decline" href="#">I AM UNDER 18 YEARS</a>
    <p class="legal">By entering this site you are agreeing to the <a href="#">terms of use</a> and <a href="#">privacy policy</a>.</p>
  </main>
</body>
</html>
```